A revolutionary website for a revolutionary construction company

I am looking for inspirations... please help me and read the attached brief

I would like to achieve a website design that is modern, premium dynamic and drives emotions. I do not want a design that can be found on a normal template. Having that said, I would also like the utilisation of Illustrations that are relation to the company’s services…. Also would like to have illustrations dynamic when you navigate on them. So a young, dynamic and parallax design website that will show off these requirements. Also to add trust, with all pages designed.

please see attachements.
Updates

Low design quality

Target Market(s)

Please read brief

Number of Pages Required

5+ page

Font styles to use
Other font styles liked:
• Futura

Requirements
Must have
• Please read brief - colours to be matching logo colours
Nice to have
Should not have

```html
<!DOCTYPE html>
<html lang="en">
<head>
<meta charset="utf-8">
<title>Ironvale Builds</title>
<link href="https://fonts.googleapis.com/css2?family=Michroma&family=Roboto:wght@400;500;700&display=swap" rel="stylesheet">
<style>
:root{
  --crimson:#9b1d4f;
  --ink:#4b4446;
  --text:#6f6a6b;
  --field:#efefef;
  --panel:#f0f0f0;
  --footer:#584f51;
  --white:#ffffff;
}
*{box-sizing:border-box;margin:0;padding:0}
html,body{width:1200px;height:4124px;overflow:hidden}
body{position:relative;background:var(--white);font-family:'Roboto',sans-serif;color:var(--text)}
.abs{position:absolute}
.display{font-family:'Michroma',sans-serif;text-transform:uppercase;letter-spacing:1px}

/* header */
.site-header{left:0;top:0;width:1200px;height:70px;background:var(--white)}
.brand{left:88px;top:8px;display:flex;align-items:center;gap:10px}
.brand-mark{width:54px;height:54px;border:2px solid var(--ink);border-radius:50%}
.brand-name{font-size:14px;color:var(--crimson);font-weight:500}
.menu-toggle{left:1088px;top:32px;width:22px}
.menu-toggle span{display:block;height:2px;background:var(--ink);margin-bottom:4px}

/* services */
.service{top:70px;width:300px;height:605px;color:var(--white);text-align:center}
.service h3{position:absolute;top:252px;left:0;width:100%;font-size:22px;font-weight:400;line-height:30px}
.service p{position:absolute;top:530px;left:20px;right:20px;font-size:13px;line-height:19px}
.service-active{left:300px;top:675px;width:300px;height:8px;background:var(--crimson)}

/* about */
.about-photo{left:300px;top:781px;width:479px;height:501px;background:linear-gradient(135deg,#6b4a3a,#a37a5c 45%,#d8d2cc)}
.about-brand{left:88px;top:998px;font-size:38px;line-height:44px;color:var(--crimson);z-index:2}
.about-title{left:836px;top:965px;font-size:30px;line-height:36px;color:var(--ink)}
.about-text{left:836px;top:1050px;width:280px;font-size:16px;line-height:23px}
.about-more{left:836px;top:1180px}

/* facts */
.section-title{font-size:34px;color:var(--ink);line-height:40px}
.facts-title{left:88px;top:1388px}
.facts-intro{left:88px;top:1440px;width:570px;font-size:16px;line-height:23px}
.facts-panel{left:88px;top:1523px;width:1112px;height:296px;background:var(--panel)}
.fact{top:1605px;width:220px;text-align:center}
.fact svg{display:block;margin:0 auto}
.fact strong{display:block;font-family:'Michroma',sans-serif;font-size:34px;color:var(--crimson);margin-top:10px;font-weight:400}
.fact span{display:block;font-size:16px;color:var(--ink);margin-top:6px;font-weight:500}

/* projects */
.projects-title{left:88px;top:1932px}
.tile{position:absolute}
.tile-feature{background:var(--crimson);color:var(--white);display:flex;flex-direction:column;align-items:center;justify-content:center}
.tile-feature .tools{display:flex;gap:8px;margin-bottom:12px}
.tile-feature .tools i{width:26px;height:26px;background:var(--white);display:block}
.tile-feature h4{font-family:'Michroma',sans-serif;font-weight:400;font-size:17px}

/* testimonials */
.testimonials-band{left:0;top:2558px;width:1200px;height:508px;background:linear-gradient(180deg,#a5abbb,#7b8296 70%,#5e6577)}
.testimonials-title{left:0;top:2676px;width:1200px;text-align:center;font-size:34px;color:var(--white)}
.avatar{top:2738px;width:50px;height:50px;border-radius:50%;background:#c9c4c0;border:2px solid var(--white)}
.quote-card{left:330px;top:2816px;width:566px;height:171px;background:var(--white)}
.quote-card .q-avatar{position:absolute;left:18px;top:30px;width:50px;height:50px;border-radius:50%;background:#cfcac7}
.quote-card .mark{position:absolute;left:82px;top:6px;font-size:60px;color:#c7c7c7;font-family:Georgia,serif}
.quote-card .who{position:absolute;left:82px;top:50px;font-size:15px;color:var(--ink)}
.quote-card .where{position:absolute;left:82px;top:70px;font-size:11px;color:#9a9a9a}
.quote-card p{position:absolute;left:82px;top:92px;width:285px;font-size:12px;line-height:17px}
.quote-card .thumb{position:absolute;top:32px;width:84px;height:113px}

/* contact */
.skyline{left:0;top:3540px;width:1200px;height:240px;background:linear-gradient(180deg,rgba(88,79,81,0) 0%,rgba(88,79,81,.85) 55%,var(--footer) 100%)}
.contact-title{left:0;top:3190px;width:1200px;text-align:center}
.field{background:var(--field);font-size:14px;color:var(--ink);padding:13px 20px;font-weight:500}
.submit{left:510px;top:3486px;width:180px;height:38px;background:var(--crimson);color:var(--white);font-weight:700;font-size:14px;display:flex;align-items:center;justify-content:center}

/* footer */
.site-footer{left:0;top:3780px;width:1200px;height:344px;background:var(--footer);color:var(--white)}
.footer-brand{left:88px;top:3850px;display:flex;align-items:center;gap:12px;color:var(--white)}
.footer-brand .mark{width:44px;height:44px;border:2px solid var(--white);border-radius:50%}
.footer-brand .name{font-size:18px;font-weight:500}
.footer-head{font-size:17px;font-weight:700}
.footer-list{font-size:12px;line-height:23px;list-style:none}
.newsletter-input{left:551px;top:3870px;width:262px;height:40px;background:var(--white);color:#888;font-size:11px;padding:13px 18px}
.newsletter-btn{left:551px;top:3920px;width:126px;height:38px;background:var(--crimson);font-size:13px;font-weight:700;display:flex;align-items:center;justify-content:center}
.contact-line{font-size:12px;line-height:17px;display:flex;gap:6px}
.social{top:3960px;width:26px;height:26px;background:rgba(255,255,255,.15)}
.social.primary{background:var(--crimson)}
.copyright{left:88px;top:4082px;font-size:12px}
.legal{left:906px;top:4082px;font-size:12px}
.to-top{left:1146px;top:4008px;width:30px;height:30px;background:var(--crimson);display:flex;align-items:center;justify-content:center}
</style>
</head>
<body>

<header class="abs site-header">
  <div class="abs brand"><div class="brand-mark"></div><div class="brand-name">Ironvale Builds</div></div>
  <div class="abs menu-toggle"><span></span><span></span><span></span></div>
</header>

<section>
  <div class="abs service" style="left:0;background:linear-gradient(180deg,#4a3c3c,#2f2c35)" role="img" aria-label="Fit-out interior photograph">
    <h3 class="display">Fit-Out</h3><p>Lorem Ipsum is simply dummy text of the printing and typesetting industry.</p></div>
  <div class="abs service" style="left:300px;background:linear-gradient(180deg,#7c7778,#433e44)" role="img" aria-label="Construction site with cranes photograph">
    <h3 class="display">Construction</h3><p>Lorem Ipsum is simply dummy text of the printing and typesetting industry.</p></div>
  <div class="abs service" style="left:600px;background:linear-gradient(180deg,#a497a3,#7c6f80)" role="img" aria-label="Project management hand with pen photograph">
    <h3 class="display">Project<br>Management</h3><p>Lorem Ipsum is simply dummy text of the printing and typesetting industry.</p></div>
  <div class="abs service" style="left:900px;background:linear-gradient(180deg,#6d6472,#3c3b52)" role="img" aria-label="Design and construct blueprint photograph">
    <h3 class="display">Design and<br>Construct</h3><p>Lorem Ipsum is simply dummy text of the printing and typesetting industry.</p></div>
  <div class="abs service-active"></div>
</section>

<section>
  <div class="abs about-photo" role="img" aria-label="Modern lounge interior photograph"></div>
  <h2 class="abs display about-brand">Ironvale<br>Builds</h2>
  <h2 class="abs display about-title">About<br>Compay</h2>
  <p class="abs about-text">Lorem Ipsum is simply dummy text of the printing and typesetting industry. Lorem Ipsum has been the industry's standard dummy text ever since the when an unknown .</p>
  <svg class="abs about-more" width="16" height="24" viewBox="0 0 16 24"><path d="M3 3l9 9-9 9" fill="none" stroke="var(--crimson)" stroke-width="3"/></svg>
</section>

<section>
  <h2 class="abs display section-title facts-title">Awesome Facts</h2>
  <p class="abs facts-intro">Many factors contribute to Ironvale Builds success. Here are some basic stats to help you understand the big picture.</p>
  <div class="abs facts-panel"></div>
  <div class="abs fact" style="left:156px">
    <svg width="64" height="54" viewBox="0 0 64 54" fill="none" stroke="#6f6a6b" stroke-width="2"><circle cx="24" cy="16" r="10"/><circle cx="42" cy="14" r="9"/><path d="M4 50c0-12 9-20 20-20s20 8 20 20z"/><path d="M46 28c8 1 14 8 14 18h-12"/></svg>
    <strong>400+</strong><span>People around australia</span></div>
  <div class="abs fact" style="left:396px">
    <svg width="58" height="58" viewBox="0 0 58 58" fill="none" stroke="#6f6a6b" stroke-width="2"><circle cx="29" cy="29" r="26"/><path d="M18 33c4 7 18 7 22 0M18 22c2-3 5-3 7 0M33 22c2-3 5-3 7 0"/></svg>
    <strong>+83</strong><span>Client SPS Score</span></div>
  <div class="abs fact" style="left:604px">
    <svg width="50" height="58" viewBox="0 0 50 58" fill="none" stroke="#6f6a6b" stroke-width="2"><path d="M18 4h14l-4 10h-6z"/><path d="M21 14C8 22 4 34 6 44c2 8 10 11 19 11s17-3 19-11c2-10-2-22-15-30z"/><path d="M30 28c-2-3-10-3-10 2s10 3 10 8-8 5-10 2M25 24v4M25 42v4"/></svg>
    <strong>742M</strong><span>National Turnover FY2020</span></div>
  <div class="abs fact" style="left:852px">
    <svg width="64" height="58" viewBox="0 0 64 58" fill="none" stroke="#6f6a6b" stroke-width="2"><path d="M4 26L32 4l28 22M10 22v34h44V22"/><rect x="38" y="10" width="8" height="10"/><circle cx="24" cy="42" r="8"/><circle cx="24" cy="42" r="3"/><rect x="36" y="30" width="12" height="12"/></svg>
    <strong>30+</strong><span>Year In the Industry</span></div>
</section>

<section>
  <h2 class="abs display section-title projects-title">Our Projects</h2>
  <div class="tile" style="left:88px;top:2011px;width:487px;height:439px;background:linear-gradient(135deg,#8a7560,#c9b59c 50%,#5f5045)" role="img" aria-label="Hotel bedroom interior photograph"></div>
  <div class="tile" style="left:589px;top:2011px;width:255px;height:213px;background:linear-gradient(180deg,#9cc4e8,#a8926a)" role="img" aria-label="Workers on building frame photograph"></div>
  <div class="tile" style="left:856px;top:2011px;width:256px;height:213px;background:linear-gradient(135deg,#6b6a70,#d27a2c 60%,#3b3d45)" role="img" aria-label="Engineers with laptop on site photograph"></div>
  <div class="tile tile-feature" style="left:589px;top:2237px;width:255px;height:213px"><div class="tools"><i></i><i></i></div><h4>HEADING HERE</h4></div>
  <div class="tile" style="left:856px;top:2237px;width:256px;height:213px;background:linear-gradient(135deg,#eef0f3,#d8dce2 55%,#e9c23a)" role="img" aria-label="Plans and safety helmet on desk photograph"></div>
</section>

<section>
  <div class="abs testimonials-band" role="img" aria-label="Living room with side table and armchair backdrop"></div>
  <h2 class="abs display testimonials-title">Testimonials</h2>
  <div class="abs avatar" style="left:433px"></div>
  <div class="abs avatar" style="left:490px"></div>
  <div class="abs avatar" style="left:547px"></div>
  <div class="abs avatar" style="left:604px"></div>
  <div class="abs avatar" style="left:661px"></div>
  <div class="abs avatar" style="left:718px"></div>
  <div class="abs quote-card">
    <div class="q-avatar"></div>
    <div class="mark">&ldquo;</div>
    <div class="who">Daniel Reyes</div>
    <div class="where">Harbor Street</div>
    <p>Lorem ipsum dolor sit amet, consectetuer adipiscing elit. Aenean commodo ligula eget dolor. Aenean massa cum sociis natoque .</p>
    <div class="thumb" style="left:374px;background:linear-gradient(180deg,#e8e4dc,#b79b6f)" role="img" aria-label="Shelf interior photograph"></div>
    <div class="thumb" style="left:464px;background:linear-gradient(180deg,#dfe3e8,#f6f6f6)" role="img" aria-label="White sofa interior photograph"></div>
  </div>
</section>

<section>
  <div class="abs skyline" role="img" aria-label="City skyline with cranes silhouette"></div>
  <h2 class="abs display section-title contact-title">Contact Us</h2>
  <div class="abs field" style="left:352px;top:3230px;width:245px;height:40px">Name</div>
  <div class="abs field" style="left:603px;top:3230px;width:246px;height:40px">Email</div>
  <div class="abs field" style="left:352px;top:3279px;width:497px;height:40px">Subject</div>
  <div class="abs field" style="left:352px;top:3328px;width:497px;height:147px">Message</div>
  <div class="abs submit">SUBMIT NOW</div>
</section>

<footer class="abs site-footer"></footer>
<div class="abs footer-brand"><div class="mark"></div><div class="name">Ironvale Builds</div></div>
<div class="abs" style="left:381px;top:3808px;color:#fff">
  <div class="footer-head">Useful Links</div>
  <ul class="footer-list" style="margin-top:8px"><li>Home</li><li>About</li><li>Services</li><li>Latest Projects</li><li>Blog</li><li>Contact Us</li></ul>
</div>
<div class="abs" style="left:551px;top:3808px;color:#fff">
  <div class="footer-head">Newsletter</div>
  <div style="font-size:12px;margin-top:10px">Subscribe to our newsletter</div>
</div>
<div class="abs newsletter-input">Enter your email address...</div>
<div class="abs newsletter-btn" style="color:#fff">SUBSCRIBE</div>
<div class="abs" style="left:876px;top:3808px;color:#fff">
  <div class="footer-head">Contact Us</div>
  <div class="contact-line" style="margin-top:10px"><svg width="10" height="14" viewBox="0 0 10 14"><path d="M5 0a5 5 0 015 5c0 4-5 9-5 9S0 9 0 5a5 5 0 015-5z" fill="#bbb"/></svg><span>4810 Oakridge Avenue,<br>Fairhaven 30219</span></div>
  <div class="contact-line" style="margin-top:6px"><svg width="12" height="10" viewBox="0 0 12 10"><rect width="12" height="10" fill="#bbb"/><path d="M0 0l6 5 6-5" fill="none" stroke="#584f51"/></svg><span>info@ironvalebuilds.com</span></div>
  <div class="contact-line" style="margin-top:4px"><svg width="12" height="12" viewBox="0 0 12 12"><path d="M2 0l3 3-2 2c1 2 2 3 4 4l2-2 3 3-2 2C5 12 0 7 0 2z" fill="#bbb"/></svg><span>555-014-2290</span></div>
</div>
<div class="abs social primary" style="left:880px"></div>
<div class="abs social" style="left:914px"></div>
<div class="abs social" style="left:948px"></div>
<div class="abs social" style="left:982px"></div>
<div class="abs social" style="left:1016px"></div>
<div class="abs to-top"><svg width="10" height="6" viewBox="0 0 10 6"><path d="M1 5l4-4 4 4" fill="none" stroke="#fff" stroke-width="1.5"/></svg></div>
<div class="abs copyright" style="color:#fff">&copy; 2020. All rights reserved.</div>
<div class="abs legal" style="color:#fff">Terms &amp; Conditions &nbsp;|&nbsp; Priacy Policy</div>

</body>
</html>
```